BPH Business Card 2018

Brellmore Chiropractic. We have two locations that we want to advertise on the same card. Calderwick OrthoAxis campus address: 3815 Pemberly Dr., Suite 240, Flowood, MS 39587. Madison address: 426 Larkmoor Dr., Building D., Madison, MS 39674. website: www.drbrellmore.example. o:(601)555-0148 f:(601)555-0173

Target Market(s)

Health care decision makers: primary care doctors and mothers

Contact Information for Business Card

I have no idea; up for any suggestions and I'd do much better picking from examples versus describing what I'm looking for. We are in a very high end location and would like the cards to look really sharp.

Requirements
Must have
• My name, Tobias R Venmark, D.C.

```html
<!DOCTYPE html>
<html lang="en">
<head>
<meta charset="utf-8">
<title>Brellmore Chiropractic – Business Card</title>
<link rel="stylesheet" href="https://fonts.googleapis.com/css2?family=Cinzel:wght@400;600&family=Tinos:ital,wght@0,400;0,700&display=swap">
<style>
  :root {
    --backdrop: #141c2b;
    --navy: #263873;
    --navy-deep: #24316b;
    --azure: #2b6db0;
    --white: #ffffff;
    --ink: #263873;
  }
  * { margin: 0; padding: 0; box-sizing: border-box; }
  html, body { width: 1200px; height: 1200px; overflow: hidden; }
  body { background: var(--backdrop); position: relative; font-family: "Cinzel", serif; }

  .card {
    position: absolute;
    left: 233px;
    width: 734px;
    height: 420px;
    box-shadow: 6px 8px 10px rgba(0,0,0,0.45);
  }
  .card--front { top: 116px; background: var(--navy); color: var(--white); }
  .card--back { top: 667px; background: var(--white); color: var(--ink); }

  .brand { position: absolute; font-weight: 600; }
  .brand__name { display: block; line-height: 1; letter-spacing: 0.5px; }
  .brand__sub { display: block; line-height: 1; }
  .brand__campus { display: block; font-family: "Tinos", serif; font-weight: 700; line-height: 1; }
  .brand__address { display: block; font-family: "Tinos", serif; text-transform: uppercase; line-height: 1; letter-spacing: 0.3px; }

  .card--front .brand { left: 354px; top: 150px; }
  .card--front .brand__name { font-size: 45px; }
  .card--front .brand__sub { font-size: 28px; margin-top: 2px; }
  .card--front .brand__campus { font-size: 13px; margin-top: 8px; }
  .card--front .brand__address { font-size: 7.5px; margin-top: 6px; font-weight: 400; }

  .card--back .brand { left: 0; right: 0; top: 44px; text-align: center; color: var(--navy); }
  .card--back .brand__name { font-size: 33px; }
  .card--back .brand__sub { font-size: 21px; margin-top: 1px; }
  .card--back .brand__campus { font-size: 10.5px; margin-top: 5px; }
  .card--back .brand__address { font-size: 6px; margin-top: 4px; font-weight: 700; }

  .doctor {
    position: absolute; left: 0; right: 0; top: 160px;
    text-align: center; font-size: 30px; font-weight: 400; letter-spacing: 1px; color: var(--navy);
  }

  .locations { position: absolute; left: 0; top: 223px; width: 734px; height: 91px; display: flex; }
  .location {
    display: flex; align-items: center; gap: 8px;
    font-size: 18px; line-height: 1.2; color: var(--white);
  }
  .location--flowood { width: 366px; background: var(--navy-deep); padding-left: 26px; }
  .location--madison { flex: 1; background: var(--azure); justify-content: flex-end; padding-right: 22px; text-align: right; }
  .location svg { width: 14px; height: 18px; flex: none; align-self: flex-start; margin-top: 3px; }

  .contact { position: absolute; left: 0; right: 0; top: 336px; text-align: center; font-size: 17px; color: var(--navy); }
  .contact__row { display: flex; justify-content: center; align-items: center; gap: 8px; line-height: 1; }
  .contact__row + .contact__row { margin-top: 12px; }
  .contact__item { display: inline-flex; align-items: center; gap: 7px; }
  .contact__item + .contact__item { margin-left: 14px; }
  .contact svg { width: 16px; height: 16px; fill: var(--navy); }
</style>
</head>
<body>

<section class="card card--front">
  <div class="brand">
    <span class="brand__name">BRELLMORE</span>
    <span class="brand__sub">CHIROPRACTIC</span>
    <span class="brand__campus">Calderwick Professional Campus</span>
    <span class="brand__address">3815 Pemberly Drive Suite 240 Flowood MS 39587</span>
  </div>
</section>

<section class="card card--back">
  <div class="brand">
    <span class="brand__name">BRELLMORE</span>
    <span class="brand__sub">CHIROPRACTIC</span>
    <span class="brand__campus">Calderwick Professional Campus</span>
    <span class="brand__address">3815 Pemberly Drive Suite 240 Flowood MS 39587</span>
  </div>

  <h1 class="doctor">TOBIAS R VENMARK, D.C.</h1>

  <div class="locations">
    <div class="location location--flowood">
      <svg viewBox="0 0 14 18" aria-hidden="true"><path fill="#fff" d="M7 0C3.1 0 0 3.1 0 7c0 5 7 11 7 11s7-6 7-11c0-3.9-3.1-7-7-7zm0 9.6A2.6 2.6 0 1 1 7 4.4a2.6 2.6 0 0 1 0 5.2z"/></svg>
      <span>3815 PEMBERLY DR., SUITE 240,<br>FLOWOOD, MS 39587</span>
    </div>
    <div class="location location--madison">
      <span>426 LARKMOOR DR., BUILDING D.,<br>MADISON, MS 39674</span>
      <svg viewBox="0 0 14 18" aria-hidden="true"><path fill="#fff" d="M7 0C3.1 0 0 3.1 0 7c0 5 7 11 7 11s7-6 7-11c0-3.9-3.1-7-7-7zm0 9.6A2.6 2.6 0 1 1 7 4.4a2.6 2.6 0 0 1 0 5.2z"/></svg>
    </div>
  </div>

  <div class="contact">
    <div class="contact__row">
      <span class="contact__item">
        <svg viewBox="0 0 16 16" aria-hidden="true"><path d="M3.2 0.8l2.3 0 1.2 3.6-1.7 1.3c0.9 1.9 2.4 3.4 4.3 4.3l1.3-1.7 3.6 1.2 0 2.3c0 1.1-0.9 2-2 2C6.5 13.8 1.2 8.5 1.2 2.8c0-1.1 0.9-2 2-2z"/></svg>
        (601)555-0148
      </span>
      <span class="contact__item">
        <svg viewBox="0 0 16 16" aria-hidden="true"><path d="M4 1h8v4H4zM1 6h14v7h-3v2H4v-2H1zm4 5v3h6v-3zm8-3.5a1 1 0 1 0 0 .01z"/></svg>
        (601)555-0173
      </span>
    </div>
    <div class="contact__row">
      <span class="contact__item">
        <svg viewBox="0 0 16 16" aria-hidden="true"><path d="M8 0a8 8 0 1 0 0 16A8 8 0 0 0 8 0zm5.9 7.2h-2.6c-.1-2-.5-3.8-1.2-5.1a6.5 6.5 0 0 1 3.8 5.1zM8 14.4c-.8-.9-1.6-2.8-1.7-5.6h3.4c-.1 2.8-.9 4.7-1.7 5.6zM6.3 7.2C6.4 4.4 7.2 2.5 8 1.6c.8.9 1.6 2.8 1.7 5.6zM5.9 2.1c-.7 1.3-1.1 3.1-1.2 5.1H2.1a6.5 6.5 0 0 1 3.8-5.1zM2.1 8.8h2.6c.1 2 .5 3.8 1.2 5.1a6.5 6.5 0 0 1-3.8-5.1zm8 5.1c.7-1.3 1.1-3.1 1.2-5.1h2.6a6.5 6.5 0 0 1-3.8 5.1z"/></svg>
        WWW.DRBRELLMORE.EXAMPLE
      </span>
    </div>
  </div>
</section>

</body>
</html>
```